ROV teaser ONE PAGER for Investors and Politicans

i require a teaser information for a company (called ROV). Teaser to contain all the necessary company information / business model. It should contain the following: 1. ROV comapny overview 2. ROV mission / vision 3. Shareholders 4. Country map 5. Company structure 6. Business activities 7. Value chain 8. Key capabilities The basis should be much like the DUL document called "dul-group-fact-sheet-january-2019.pdf". document (dul-group-fact-sheet-january-2019.pdf) - it. (rov teaser One pager.pptx) document can not look / feel the same. The key information to place in the ROV TEASER document is the following document "2019_04_12_ROV Teaser for BTorvan". It contains all the necessary information to set up the one page - but unfortunately its on multiple power point pages.

Target Market(s)

external customers and investors and high ranking poilticans

Industry/Entity Type

Oil And Gas

Font styles to use
Other font styles liked:
• see script from the website of ROV

Colors

Designer to choose colors to be used in the design.

Requirements
Must have
• in the document called "ROV Teaser One PAGER" - must be powerpoint format - the rough style should be kept in the middle of this document
Nice to have
• - to have mutiple version in powerpoint format - wide screen format in 16x9
Should not have
• N / A

```html
<!DOCTYPE html>
<html lang="en">
<head>
<meta charset="utf-8">
<title>ROV Energy – Teaser One Pager</title>
<link href="https://fonts.googleapis.com/css2?family=Roboto:wght@300;400;500;700&display=swap" rel="stylesheet">
<style>
:root{
  --red:#d20a11;
  --red-dark:#a3070c;
  --ink:#222222;
  --text:#333333;
  --muted:#666666;
  --line:#e3e3e3;
  --footer:#1f1f1f;
  --white:#ffffff;
}
*{box-sizing:border-box;margin:0;padding:0}
html,body{width:847px;height:1200px;overflow:hidden;background:var(--white)}
body{position:relative;font-family:"Roboto",Arial,sans-serif;color:var(--text)}
.header{position:absolute;left:0;top:0;width:847px;height:78px}
.header-shade{position:absolute;left:0;top:60px;width:847px;height:18px;background:linear-gradient(#c9c9c9,#ffffff)}
.header-deco{position:absolute;right:0;top:0}
.brand{position:absolute;left:16px;top:20px;display:flex;align-items:center;gap:8px}
.brand-mark{width:14px;height:14px;background:var(--red)}
.brand-name{font-weight:700;font-size:27px;color:var(--red);letter-spacing:.5px}
.tagline{position:absolute;left:219px;top:18px;font-weight:700;font-size:13.4px;line-height:15px;color:var(--ink)}
.intro{position:absolute;left:16px;top:88px;width:520px}
.section-title{font-weight:700;font-size:17.5px;color:var(--red);text-transform:uppercase;margin-bottom:4px}
.intro p{font-size:9px;line-height:11.2px;color:var(--ink)}
.intro .block{margin-bottom:8px}
.hl{color:var(--red);font-weight:700}
.map{position:absolute;left:542px;top:70px;width:305px;height:225px;background:radial-gradient(ellipse at 55% 50%,#d6d6d6 0%,#e2e2e2 55%,#ffffff 80%)}
.focus{position:absolute;left:14px;top:302px;width:816px;border-collapse:collapse;table-layout:fixed}
.focus th{background:linear-gradient(#e01017,var(--red-dark));color:var(--white);font-weight:700;font-size:16px;height:33px;text-transform:uppercase;border-right:2px solid var(--white)}
.focus td{border-bottom:1px solid var(--line);border-right:1px solid var(--line);font-size:8.6px;line-height:10.4px;color:var(--ink);padding:10px 16px 4px 11px;vertical-align:top}
.focus td.area{text-align:center;vertical-align:middle;font-size:11px;line-height:14px;color:var(--ink);padding:6px}
.focus td.area svg{display:block;margin:0 auto 6px}
.traction-title{position:absolute;left:16px;top:888px}
.traction-note{position:absolute;left:16px;top:912px;font-size:9px;color:var(--ink)}
.gallery{position:absolute;left:14px;top:932px;display:flex;gap:20px}
.photo{position:relative;width:146px;height:68px}
.photo .caption{position:absolute;left:0;bottom:0;width:100%;height:17px;background:rgba(210,10,17,.88);color:var(--white);font-size:9.5px;text-align:center;line-height:17px}
.p1{background:linear-gradient(#8fb3cc,#6f9a6a)}
.p2{background:linear-gradient(#c9a56a,#3e4d5c)}
.p3{background:linear-gradient(#cfe0ee,#b27a4a)}
.p4{background:linear-gradient(#a8b0a4,#6d7a5a)}
.p5{background:linear-gradient(#b89a6e,#5f7a45)}
.mgmt-title{position:absolute;left:16px;top:1013px}
.team{position:absolute;left:0;top:1043px;width:847px}
.member{position:absolute;width:160px;text-align:center}
.avatar{width:64px;height:64px;border-radius:50%;background:#eeeeee;margin:0 auto 6px}
.member .name{font-weight:700;font-size:11px;color:var(--ink)}
.member .role{font-size:8px;color:var(--red)}
.member .exp{font-size:9.5px;color:var(--muted)}
.footer{position:absolute;left:0;top:1159px;width:847px;height:41px;background:var(--footer)}
.footer svg{position:absolute;left:0;top:0}
.contact{position:absolute;right:18px;top:12px;color:var(--white);font-size:13px}
</style>
</head>
<body>
<header class="header">
  <div class="header-shade"></div>
  <svg class="header-deco" width="360" height="78" viewBox="0 0 360 78">
    <polygon points="150,0 360,0 360,78 300,78" fill="#ececec"/>
    <polygon points="200,0 360,0 360,60 280,60" fill="#d20a11"/>
    <polygon points="260,0 360,0 360,30" fill="#a3070c"/>
    <polygon points="230,60 360,60 360,78 250,78" fill="#e9e9e9"/>
  </svg>
  <div class="brand"><span class="brand-mark"></span><span class="brand-name">ROV ENERGY</span></div>
  <p class="tagline">We work on the forefront of innovation and technology to<br>take products from an idea all the way to the end consumer</p>
</header>

<section class="intro">
  <div class="block">
    <h2 class="section-title">Executive Summary</h2>
    <p><span class="hl">ROV Group</span> Ltd is the shareholder of ROV Energy Ltd (registration code 04718293).</p>
    <p><span class="hl">ROV</span> has subsidiaries in the Republic of Moldova – Otaci Free Zone and Ukraine – Harkov/Kiev.</p>
    <p>Plans are to set up or acquire new subsidiaries in Austria, Hungary, Italy, Slovakia, Macedonia and others,<br>depending on the market conditions. Moreover, the company has a branch in Romania, Bucharest.</p>
    <p><span class="hl">ROV ENERGY</span> is active in trading (import and export) of natural gas across the Eastern European market.</p>
  </div>
  <div class="block">
    <h2 class="section-title">Vision</h2>
    <p>Increasing the market share by developing potential gas trading business line partners from<br>Romania and regional countries such as Greece, Hungary, Austria and Italy</p>
  </div>
  <div class="block">
    <h2 class="section-title">Strengths</h2>
    <p>Xx highly committed individuals, strong market position via various commodities,<br>sophisticated trading and risk management capability</p>
  </div>
</section>

<div class="map" role="img" aria-label="Map of Europe highlighting Austria, Hungary, Italy and Greece"></div>

<table class="focus">
  <colgroup><col style="width:156px"><col style="width:330px"><col style="width:330px"></colgroup>
  <thead><tr><th>Focus Areas</th><th>Relevant Data</th><th>Details</th></tr></thead>
  <tbody>
    <tr style="height:108px">
      <td class="area"><svg width="40" height="22" viewBox="0 0 40 22" fill="none" stroke="#444" stroke-width="1.2"><path d="M2 14h36M2 18h36M8 14V8h6v6M26 14V8h6v6M20 4v6"/><circle cx="20" cy="3" r="2"/></svg>Oil &amp; Gas Midstream</td>
      <td>Lorem Ipsum is simply dummy text of the printing and typesetting industry. Lorem Ipsum has been the industry's standard dummy text ever since the 1500s, when an unknown printer took a galley of type and scrambled it to make a type specimen book. It has survived not only five centuries, but also the leap into electronic typesetting, remaining essentially unchanged. It was popularised in the 1960s with the release of Letraset sheets containing Lorem Ipsum</td>
      <td>Lorem Ipsum is simply dummy text of the printing and typesetting industry. Lorem Ipsum has been the industry's standard dummy text ever since the 1500s, when an unknown printer took a galley of type and scrambled it to make a type specimen book. It has survived not only five centuries, but also the leap into electronic typesetting, remaining essentially unchanged. It was popularised in the 1960s</td>
    </tr>
    <tr style="height:86px">
      <td class="area"><svg width="40" height="22" viewBox="0 0 40 22" fill="none" stroke="#444" stroke-width="1.2"><path d="M4 20h32M24 20V10l6-6 6 6v10M6 10h8M8 6l4 8M12 6l-4 8"/></svg>Conventional Power</td>
      <td>Lorem Ipsum is simply dummy text of the printing and typesetting industry. Lorem Ipsum has been the industry's standard dummy text ever since the 1500s, when an unknown printer took a galley of type and scrambled it to make a type specimen book. It has survived not only five centuries, but also the leap into electronic typesetting, remaining essentially unchanged. It was popularised in the 1960s</td>
      <td>Lorem Ipsum is simply dummy text of the printing and typesetting industry. Lorem Ipsum has been the industry's standard dummy text ever since the 1500s, when an unknown printer took a galley of type and scrambled it to make a type specimen book. It has survived not only five centuries, but also the leap into electronic typesetting, remaining essentially unchanged. It was popularised in the 1960s</td>
    </tr>
    <tr style="height:90px">
      <td class="area"><svg width="40" height="24" viewBox="0 0 40 24" fill="none" stroke="#444" stroke-width="1.2"><path d="M10 22l8-16 8 16M13 16h10M18 2v4"/><path d="M32 8c-2 3-3 5-3 6a3 3 0 006 0c0-1-1-3-3-6z" fill="#444"/></svg>Oil and Gas</td>
      <td>Lorem Ipsum is simply dummy text of the printing and typesetting industry. Lorem Ipsum has been the industry's standard dummy text ever since the 1500s, when an unknown printer took a galley of type and scrambled it to make a type specimen book. It has survived not only five centuries, but also the leap into electronic typesetting, remaining essentially unchanged. It was popularised in the 1960s with the release of Letraset sheets containing Lorem Ipsum</td>
      <td>Lorem Ipsum is simply dummy text of the printing and typesetting industry. Lorem Ipsum has been the industry's standard dummy text ever since the 1500s, when an unknown printer took a galley of type and scrambled it to make a type specimen book. It has survived not only five centuries, but also the leap into electronic typesetting, remaining essentially unchanged. It was popularised in the 1960s with the release of Letraset sheets containing Lorem Ipsum</td>
    </tr>
    <tr style="height:91px">
      <td class="area"><svg width="40" height="22" viewBox="0 0 40 22" fill="none" stroke="#444" stroke-width="1.2"><path d="M4 20V8h4v4l5-4v4l5-4v12zM4 20h32M26 20V6h8v14M26 10h8M26 14h8"/></svg>Electricity Demand</td>
      <td>Lorem Ipsum is simply dummy text of the printing and typesetting industry. Lorem Ipsum has been the industry's standard dummy text ever since the 1500s, when an unknown printer took a galley of type and scrambled it to make a type specimen book. It has survived not only five centuries, but also the leap into electronic typesetting, remaining essentially unchanged. It was popularised in the 1960s with the release of Letraset sheets containing Lorem Ipsum</td>
      <td>Lorem Ipsum is simply dummy text of the printing and typesetting industry. Lorem Ipsum has been the industry's standard dummy text ever since the 1500s, when an unknown printer took a galley of type and scrambled it to make a type specimen book. It has survived not only five centuries, but also the leap into electronic typesetting, remaining essentially unchanged. It was popularised in the 1960s</td>
    </tr>
    <tr style="height:85px">
      <td class="area"><svg width="40" height="22" viewBox="0 0 40 22" fill="none" stroke="#444" stroke-width="1.2"><path d="M2 18l4-8h16l4 8zM9 10l-2 8M15 10v8M21 10l2 8M4 14h20"/><circle cx="16" cy="5" r="2.5"/><path d="M32 20V8M32 8l-4-4M32 8l5-1M32 8l-1 5"/></svg>Renewables</td>
      <td>Lorem Ipsum is simply dummy text of the printing and typesetting industry. Lorem Ipsum has been the industry's standard dummy text ever since the 1500s, when an unknown printer took a galley of type and scrambled it to make a type specimen book. It has survived not only five centuries, but also the leap into electronic typesetting, remaining essentially unchanged. It was popularised in the 1960s</td>
      <td>Lorem Ipsum is simply dummy text of the printing and typesetting industry. Lorem Ipsum has been the industry's standard dummy text ever since the 1500s, when an unknown printer took a galley of type and scrambled it to make a type specimen book. It has survived not only five centuries, but also the leap into electronic typesetting,</td>
    </tr>
    <tr style="height:85px">
      <td class="area"><svg width="40" height="26" viewBox="0 0 40 26" fill="none" stroke="#444" stroke-width="1.2"><path d="M14 24l6-22 6 22M16 16h8M17 10h6M10 6h20M12 11h16"/></svg>Transmission and<br>Distribution</td>
      <td>Lorem Ipsum is simply dummy text of the printing and typesetting industry. Lorem Ipsum has been the industry's standard dummy text ever since the 1500s, when an unknown printer took a galley of type and scrambled it to make a type specimen book. It has survived not only five centuries, but also the leap into electronic typesetting, remaining essentially unchanged. It was popularised in the 1960s</td>
      <td>Lorem Ipsum is simply dummy text of the printing and typesetting industry. Lorem Ipsum has been the industry's standard dummy text ever since the 1500s, when an unknown printer took a galley of type and scrambled it to make a type specimen book. It has survived not only five centuries, but also the leap into electronic typesetting, remaining essentially unchanged. It was popularised in the 1960s</td>
    </tr>
  </tbody>
</table>

<h2 class="section-title traction-title">Traction from ROV</h2>
<p class="traction-note">ROV operates at XX countries/locations or regions around the world:</p>
<div class="gallery">
  <div class="photo p1" role="img" aria-label="Aerial photo of an industrial energy site"><span class="caption">XXX</span></div>
  <div class="photo p2" role="img" aria-label="Photo of a solar installation in autumn hills"><span class="caption">XXX</span></div>
  <div class="photo p3" role="img" aria-label="Photo of a water reservoir"><span class="caption">XXX</span></div>
  <div class="photo p4" role="img" aria-label="Aerial photo of a power plant"><span class="caption">Power plants</span></div>
  <div class="photo p5" role="img" aria-label="Aerial photo of a construction site"><span class="caption">XXX</span></div>
</div>

<h2 class="section-title mgmt-title">Management</h2>
<div class="team">
  <div class="member" style="left:5px"><div class="avatar"></div><p class="name">NR</p><p class="role">CEO</p><p class="exp">20+years exprience XX</p></div>
  <div class="member" style="left:222px"><div class="avatar"></div><p class="name">NR</p><p class="role">CRM</p><p class="exp">20+years exprience XX</p></div>
  <div class="member" style="left:438px"><div class="avatar"></div><p class="name">NR</p><p class="role">Chief Legal Counsel</p><p class="exp">20+years exprience XX</p></div>
  <div class="member" style="left:655px"><div class="avatar"></div><p class="name">NR</p><p class="role">COO</p><p class="exp">20+years exprience XX</p></div>
</div>

<footer class="footer">
  <svg width="260" height="41" viewBox="0 0 260 41">
    <polygon points="0,20 30,0 110,0 70,41 0,41" fill="#a3070c"/>
    <polygon points="60,41 100,0 160,0 120,41" fill="#d20a11"/>
    <polygon points="130,41 170,0 240,0 200,41" fill="#d20a11"/>
  </svg>
  <p class="contact">Contact: XXXX</p>
</footer>
</body>
</html>
```